Profesional personal website needs design and business card

I need a business card with my professional name as a logo "Marlo Vitality" for my business. I am a Wellness Coach, consultant and trainer. So it should be professional, wellness oriented and modern.

Target Market(s)

Private clients, governments, corporations. Luxury and high market.

Industry/Entity Type

Health And Wellness

Contact Information for Business Card

Marlo Vitality should be the logo

Colors

Designer to choose colors to be used in the design.

Requirements
Must have
• Marlo Vitality
• Name: Tomás Arribal
• Wellness Coach, Consultant & Trainer.
• Website: www.marlovitality.example
• Phone:
• Spain (+34) 612 480 397
• (USA) +1 (555) 318 2046
Nice to have
• The most important is the design of "Marlo Vitality", as this is going to be my personal brand logo. It should be professional, wellness, high end and actual.
Should not have
• no golds, no baroque style..

```html
<!DOCTYPE html>
<html lang="en">
<head>
<meta charset="utf-8">
<title>Marlo Vitality – Business Card</title>
<link href="https://fonts.googleapis.com/css2?family=Roboto:wght@400;500;700&display=swap" rel="stylesheet">
<style>
  :root {
    --navy: #27225f;
    --white: #ffffff;
    --ink: #000000;
    --backdrop: #7d8a8f;
    --backdrop-light: #b9c6cb;
  }
  * { box-sizing: border-box; margin: 0; padding: 0; }
  html, body {
    width: 1200px; height: 900px; overflow: hidden;
  }
  body {
    background: radial-gradient(circle at 50% 45%, var(--backdrop-light), var(--backdrop) 75%);
    font-family: "Roboto", Arial, sans-serif;
    position: relative;
  }
  .card {
    position: absolute;
    left: 280px;
    width: 640px;
    height: 366px;
    border-radius: 22px;
    overflow: hidden;
    box-shadow: 0 10px 24px rgba(0,0,0,0.28);
  }
  .card-back { top: 64px; background: var(--navy); }
  .card-front { top: 470px; background: var(--navy); }

  .brand-name {
    font-family: "Roboto", Arial, sans-serif;
    font-weight: 500;
    letter-spacing: 0.04em;
    text-transform: uppercase;
    white-space: nowrap;
  }
  .card-back .brand {
    position: absolute; left: 0; right: 0; top: 140px;
    display: flex; justify-content: center; align-items: center; gap: 16px;
  }
  .card-back .brand-mark { width: 22px; height: 22px; background: var(--white); }
  .card-back .brand-name { color: var(--white); font-size: 44px; }
  .card-back .website {
    position: absolute; left: 0; right: 0; bottom: 44px;
    text-align: center; color: var(--white); font-size: 14px; letter-spacing: 0.02em;
  }

  .card-front .shape { position: absolute; inset: 0; }
  .card-front .brand {
    position: absolute; left: 330px; width: 300px; top: 160px;
    display: flex; justify-content: center; align-items: center; gap: 12px;
  }
  .card-front .brand-mark { width: 16px; height: 16px; background: var(--navy); }
  .card-front .brand-name { color: var(--navy); font-size: 30px; }

  .contact {
    position: absolute; left: 48px; top: 150px; color: var(--white);
  }
  .contact .person { font-weight: 700; font-size: 22px; }
  .contact .role { font-size: 11px; margin-top: 4px; letter-spacing: 0.01em; }
  .contact .lines { margin-top: 26px; font-size: 16px; line-height: 1.45; }
  .contact .lines .label { display: inline-block; width: 56px; }
</style>
</head>
<body>
  <section class="card card-back">
    <div class="brand">
      <span class="brand-mark"></span>
      <span class="brand-name">Marlo Vitality</span>
    </div>
    <p class="website">www.marlovitality.example</p>
  </section>

  <section class="card card-front">
    <svg class="shape" width="640" height="366" viewBox="0 0 640 366" aria-hidden="true">
      <circle cx="548" cy="114" r="292" fill="var(--ink)"/>
      <circle cx="566" cy="108" r="290" fill="var(--white)"/>
    </svg>
    <div class="contact">
      <p class="person">Tomás Arribal</p>
      <p class="role">Wellness Coach, Consultant &amp; Trainer</p>
      <div class="lines">
        <p><span class="label">Spain</span>(+34) 612 480 397</p>
        <p><span class="label">USA</span>+1 (555) 318 2046</p>
        <p>www.marlovitality.example</p>
      </div>
    </div>
    <div class="brand">
      <span class="brand-mark"></span>
      <span class="brand-name">Marlo Vitality</span>
    </div>
  </section>
</body>
</html>
```